Fernwillow needs product labels for deodorant line, and future soap, and lip balm line.

Fernwillow is a new startup that at this time is looking for labels for our deodorant line. There will be future work for our other products given to the winning designer. Our products are all-natural free from petrochemicals, propylene glycol, parabens, aluminum compounds, or synthetic colorants. All our products are also handmade.
We are using a standard size stick to contain the product, on the front cap the label is 2"W x 1"H, on the body front and back the size is 2" W x 2.675" H. We want the front to say "aluminum free", and "all-natural deodorant"
The back needs to include, a UPC, Our mission is to bring you effective, all-natural products using the highest quality ingredients. , Ingredients Cocoa Butter, Shea Butter, Arrowroot Powder, Sodium Bicarbonate, Olive Oil, Water.
We are launching 4 scents.
scent free
Lavander
Tea Tree
Baby Powder
We included a couple pics of product labels we like but are definitely not limited to them. also a picture of the empty container.
Updates
Project Deadline Extended
Reason: Someone completed their design but didn't post it in time and asked me to extend the dead line.
Target Market(s)
Females that are health conscience.
Industry/Entity Type
Cosmetics

```html
<!DOCTYPE html>
<html lang="en">
<head>
<meta charset="utf-8">
<title>Fernwillow Lavander Deodorant Labels</title>
<link rel="stylesheet" href="https://fonts.googleapis.com/css2?family=Cinzel:wght@400;600&family=Overlock:wght@700;900&family=Marcellus&family=Lato:wght@400;700&display=swap">
<style>
  :root {
    --page: #ece9e4;
    --label-white: #ffffff;
    --purple-deep: #3e1d5c;
    --purple-band: #5b2d82;
    --purple-strip: #4a2270;
    --purple-text: #6b2fa0;
    --lavender-mist: #d9c6ec;
    --lavender-soft: #f4eefa;
    --pink-free: #e21a8c;
    --green-sage: #6a7a35;
    --green-dark: #3f4d22;
    --rule-light: #b99ad6;
  }
  * { box-sizing: border-box; margin: 0; padding: 0; }
  html, body {
    width: 1200px; height: 900px; overflow: hidden;
    background: var(--page);
  }
  .canvas {
    width: 1200px; height: 900px;
    display: flex; flex-direction: column; align-items: center; justify-content: center;
    gap: 30px;
  }

  /* Cap label: 2" x 1" */
  .cap-label {
    position: relative;
    width: 400px; height: 200px;
    background: var(--label-white);
    box-shadow: 0 2px 8px rgba(0,0,0,0.12);
    overflow: hidden;
  }
  .cap-label .scent {
    position: absolute; left: 26px; top: 34px;
    font-family: "Overlock", sans-serif; font-weight: 900;
    font-size: 46px; color: var(--purple-text);
  }
  .cap-label .claim {
    position: absolute; left: 26px; top: 104px;
    font-family: "Marcellus", serif;
    font-size: 20px; letter-spacing: 1px; color: var(--green-sage);
  }
  .cap-label .rule {
    position: absolute; left: 26px; top: 132px;
    width: 180px; height: 1.5px; background: var(--green-sage);
  }
  .cap-label .product {
    position: absolute; left: 26px; top: 138px;
    font-family: "Marcellus", serif;
    font-size: 29px; letter-spacing: 1px; color: var(--green-dark);
  }
  .cap-label .sprig-photo {
    position: absolute; right: 0; top: 0;
    width: 190px; height: 200px;
    background:
      radial-gradient(ellipse at 45% 62%, #7a4fb0 0%, #9b79c9 38%, rgba(255,255,255,0) 70%),
      linear-gradient(210deg, #9fb677 0%, rgba(255,255,255,0) 40%);
  }

  /* Body label: 2" x 2.675" */
  .body-label {
    position: relative;
    width: 400px; height: 535px;
    background: var(--label-white);
    box-shadow: 0 2px 8px rgba(0,0,0,0.12);
    overflow: hidden;
  }
  .headline-band {
    position: absolute; left: 0; top: 0;
    width: 400px; height: 132px;
    background: linear-gradient(180deg, var(--purple-deep) 0%, var(--purple-band) 55%, #7a4ca6 100%);
  }
  .headline-band .aluminum {
    position: absolute; left: 0; right: 0; top: 20px;
    text-align: center;
    font-family: "Cinzel", serif; font-weight: 400;
    font-size: 50px; letter-spacing: 0.5px; color: #ffffff;
  }
  .headline-band .free {
    position: absolute; right: 34px; top: 80px;
    width: 104px; height: 44px;
    background: var(--pink-free);
    font-family: "Cinzel", serif; font-weight: 400;
    font-size: 32px; line-height: 44px; text-align: center; color: #ffffff;
  }
  .headline-band .flourish {
    position: absolute; left: 88px; top: 92px;
    width: 150px; height: 22px;
    background: linear-gradient(90deg, rgba(255,255,255,0) 0%, rgba(255,255,255,0.55) 50%, rgba(255,255,255,0) 100%);
    border-radius: 11px;
  }
  .claim-strip {
    position: absolute; left: 0; top: 132px;
    width: 400px; height: 76px;
    background: var(--purple-strip);
    border-top: 2px solid var(--rule-light);
    border-bottom: 2px solid var(--rule-light);
    display: flex; align-items: center; justify-content: center;
    font-family: "Lato", sans-serif; font-weight: 400;
    font-size: 25px; color: #ffffff;
  }
  .scent-panel {
    position: absolute; left: 0; top: 208px;
    width: 400px; height: 327px;
    background: linear-gradient(180deg, var(--lavender-mist) 0%, var(--lavender-soft) 45%, #ffffff 100%);
  }
  .scent-panel .scent {
    position: absolute; left: 0; right: 0; top: 38px;
    text-align: center;
    font-family: "Overlock", sans-serif; font-weight: 900;
    font-size: 54px; color: var(--purple-text);
  }
  .scent-panel .flower-photo {
    position: absolute; left: 36px; top: 130px;
    width: 300px; height: 170px;
    background:
      radial-gradient(ellipse at 50% 50%, #8a5bc9 0%, #a985dc 40%, rgba(255,255,255,0) 72%),
      radial-gradient(ellipse at 10% 70%, #5c7a3a 0%, rgba(255,255,255,0) 35%);
  }
</style>
</head>
<body>
  <main class="canvas">
    <section class="cap-label" aria-label="Cap label">
      <div class="scent">Lavander</div>
      <div class="claim">ALL - NATURAL</div>
      <div class="rule"></div>
      <div class="product">DEODORA</div>
      <div class="sprig-photo" role="img" aria-label="Photo of fresh lavender sprigs"></div>
    </section>

    <section class="body-label" aria-label="Body front label">
      <div class="headline-band">
        <div class="aluminum">ALUMINUM</div>
        <div class="flourish" role="img" aria-label="Decorative flower flourish"></div>
        <div class="free">FREE</div>
      </div>
      <div class="claim-strip">All-Natural Deodora</div>
      <div class="scent-panel">
        <div class="scent">Lavander</div>
        <div class="flower-photo" role="img" aria-label="Photo of purple flowers with green leaves"></div>
      </div>
    </section>
  </main>
</body>
</html>
```